We need an attractive business card design that is modern and inviting. We like the blue and yellow (or gold) colors that are displayed with the logo. The business should communicate trust, experience, and integrity.

Target Market(s)

Residential and Commercial

Industry/Entity Type

Business

Contact Information for Business Card

Recessed Lighting
LED Retro Fit
Sign Repair
Alarms and Cameras
Mobile Home Services
24hr service calls

Font styles to use
Serif
Sans Serif

Colors
3176b5
0455a3
fece3e
fbee3e

Requirements
Must have
• Brondle Electric
• Owner: Marcus Tivane
• Licensed and Insured
• TECL #58917
Nice to have
• Exquisite Detail!!
• Over 20 years of experience
Should not have
• Nothing boring or traditional!!!

```html
<!DOCTYPE html>
<html lang="en">
<head>
<meta charset="utf-8">
<title>Brondle Electric – Business Card</title>
<link href="https://fonts.googleapis.com/css2?family=Arimo:wght@400;700&display=swap" rel="stylesheet">
<style>
  :root {
    --stage: #4b4b4d;
    --card-white: #ffffff;
    --brand-blue: #0455a3;
    --brand-mid: #3176b5;
    --brand-yellow: #fbee3e;
    --brand-gold: #fece3e;
    --ring-faint: #b9d0e8;
    --text-white: #ffffff;
  }
  * { box-sizing: border-box; margin: 0; padding: 0; }
  html, body { width: 1200px; height: 1000px; overflow: hidden; }
  body {
    background: var(--stage);
    font-family: "Arimo", Arial, sans-serif;
    position: relative;
  }

  /* ---------- Front of card ---------- */
  .card-front {
    position: absolute;
    left: 112px; top: 108px;
    width: 630px; height: 349px;
    background: var(--card-white);
    border-radius: 16px;
    overflow: hidden;
    color: var(--brand-blue);
  }
  .front-mark {
    position: absolute; left: 254px; top: 132px;
  }
  .card-front .mark-circle { position: absolute; left: 142px; top: 24px; }
  .card-front .brand-name {
    position: absolute; left: 31px; top: 104px;
    font-size: 31px; font-weight: 700; letter-spacing: 0.5px;
    color: var(--brand-blue);
  }
  .faint-ring { position: absolute; left: 392px; top: 24px; }
  .owner-name {
    position: absolute; left: 31px; top: 186px;
    font-size: 23px; font-weight: 700; letter-spacing: 1px;
  }
  .name-rule {
    position: absolute; left: 31px; top: 219px;
    width: 599px; height: 1px; background: var(--brand-gold);
  }
  .address {
    position: absolute; left: 32px; top: 228px;
    font-size: 14.5px; line-height: 18px;
  }
  .contact-line {
    position: absolute; left: 32px;
    font-size: 16px; display: flex; align-items: center; gap: 7px;
  }
  .contact-line.phone { top: 269px; }
  .contact-line.email { top: 291px; }
  .license {
    position: absolute; right: 16px; top: 292px;
    font-size: 14.5px; letter-spacing: 0.3px;
  }
  .web-band {
    position: absolute; left: 0; bottom: 0;
    width: 100%; height: 32px;
    background: var(--brand-blue);
    color: var(--text-white);
    text-align: center;
    font-size: 15.5px; font-weight: 700; letter-spacing: 1.2px;
    line-height: 30px;
  }

  /* ---------- Back of card ---------- */
  .card-back {
    position: absolute;
    left: 475px; top: 543px;
    width: 645px; height: 352px;
    border-radius: 16px;
    overflow: hidden;
    background: radial-gradient(ellipse at 52% 45%, #2b7cc6 0%, #1965b4 45%, var(--brand-blue) 100%);
    color: var(--text-white);
  }
  .side-bar {
    position: absolute; top: 26px;
    width: 14px; height: 300px;
    background: var(--brand-yellow);
  }
  .side-bar.left { left: 0; border-radius: 0 8px 8px 0; }
  .side-bar.right { right: 0; border-radius: 8px 0 0 8px; }
  .card-back .mark-circle { position: absolute; left: 276px; top: 36px; }
  .card-back .brand-name {
    position: absolute; left: 0; right: 0; top: 149px;
    text-align: center;
    font-size: 43px; font-weight: 700; letter-spacing: 1px;
    color: var(--text-white);
  }
  .services {
    position: absolute; left: 0; right: 0; top: 255px;
    text-align: center;
    font-size: 15px; font-weight: 700; letter-spacing: 0.4px; line-height: 22px;
  }
  .services .dot {
    display: inline-block; width: 7px; height: 7px; border-radius: 50%;
    background: var(--brand-yellow); margin: 0 3px; vertical-align: 2px;
  }
  .experience {
    position: absolute; left: 0; right: 0; top: 314px;
    display: flex; justify-content: center; align-items: center; gap: 8px;
    font-size: 15px; font-weight: 700; letter-spacing: 0.5px;
  }
  .experience .tick-line {
    width: 20px; height: 2px; background: var(--brand-yellow);
  }
</style>
</head>
<body>

  <section class="card-front" aria-label="Business card front">
    <svg class="faint-ring" width="236" height="236" viewBox="0 0 236 236" aria-hidden="true">
      <circle cx="118" cy="118" r="108" fill="none" stroke="var(--ring-faint)" stroke-width="14" opacity="0.75"/>
    </svg>
    <svg class="mark-circle" width="78" height="78" viewBox="0 0 78 78" aria-hidden="true">
      <circle cx="39" cy="39" r="35" fill="none" stroke="var(--brand-blue)" stroke-width="6"/>
    </svg>
    <div class="brand-name">BRONDLE ELECTRIC</div>

    <div class="owner-name">Marcus Tivane</div>
    <div class="name-rule"></div>
    <div class="address">4820 Mill Creek Rd<br>Harlow, Texas</div>

    <div class="contact-line phone">
      <svg width="16" height="16" viewBox="0 0 16 16" aria-hidden="true">
        <circle cx="8" cy="8" r="7" fill="none" stroke="var(--brand-gold)" stroke-width="1.4"/>
        <path d="M5.2 4.3 l1.4 -0.3 l0.8 1.9 l-0.9 0.7 a5 5 0 0 0 2.9 2.9 l0.7 -0.9 l1.9 0.8 l-0.3 1.4 a6.5 6.5 0 0 1 -6.5 -6.5z" fill="var(--brand-gold)"/>
      </svg>
      <span>936-555-0148</span>
    </div>
    <div class="contact-line email">
      <svg width="16" height="12" viewBox="0 0 16 12" aria-hidden="true">
        <rect x="0.5" y="1" width="14" height="10" fill="var(--brand-gold)"/>
        <path d="M0.5 1 L7.5 7 L14.5 1" fill="none" stroke="#fff" stroke-width="1.2"/>
      </svg>
      <span>hello@brondleelectric.com</span>
    </div>
    <div class="license">Licensed and Insured TECL #58917</div>

    <div class="web-band">www.brondleelectric.com</div>
  </section>

  <section class="card-back" aria-label="Business card back">
    <div class="side-bar left"></div>
    <div class="side-bar right"></div>
    <svg class="mark-circle" width="112" height="112" viewBox="0 0 112 112" aria-hidden="true">
      <circle cx="56" cy="56" r="50" fill="none" stroke="var(--text-white)" stroke-width="8"/>
    </svg>
    <div class="brand-name">BRONDLE ELECTRIC</div>

    <div class="services">
      Residential and Commercial<span class="dot"></span>Recessed Lighting<span class="dot"></span>LED Retro Fit<span class="dot"></span>Sign Repair<br>
      Alarms and Cameras<span class="dot"></span>Mobile Home Services<span class="dot"></span>24hr service calls
    </div>
    <div class="experience">
      <span class="tick-line"></span>
      <span>Over 20 years of Experience</span>
      <span class="tick-line"></span>
    </div>
  </section>

</body>
</html>
```